Business Card and Stationary
BrookLamp Consutling
Professional
Peter Varsiklo
8276 Wimbrell Lane
Dublin, OH 43092
pvarsiklo@brooklampconsulting.com
brooklampconsulting.com

```html
<!DOCTYPE html>
<html lang="en">
<head>
<meta charset="utf-8">
<title>BrookLamp Consulting – Business Card</title>
<link rel="stylesheet" href="https://fonts.googleapis.com/css2?family=Source+Sans+3:wght@400;600&display=swap">
<style>
  :root {
    --backdrop: #ecebe8;
    --card: #ffffff;
    --brand-green: #7dc242;
    --ink: #3d3d3d;
    --ink-soft: #555555;
    --rule: #c9c9c9;
  }
  * { margin: 0; padding: 0; box-sizing: border-box; }
  html, body {
    width: 1200px;
    height: 778px;
    overflow: hidden;
    background: var(--backdrop);
    font-family: "Source Sans 3", "Myriad Pro", Arial, sans-serif;
  }
  .business-card {
    position: absolute;
    left: 166px;
    top: 137px;
    width: 868px;
    height: 504px;
    background: var(--card);
    border-radius: 34px;
    overflow: hidden;
    box-shadow: 0 2px 6px rgba(0,0,0,0.12);
  }
  .accent-band {
    position: absolute;
    left: 74px;
    width: 720px;
    height: 34px;
    background: var(--brand-green);
    border-radius: 17px;
  }
  .accent-band--top { top: -2px; border-top-left-radius: 0; border-top-right-radius: 0; }
  .accent-band--bottom { bottom: -2px; border-bottom-left-radius: 0; border-bottom-right-radius: 0; }

  .brand {
    position: absolute;
    left: 40px;
    width: 340px;
    top: 196px;
    text-align: center;
    color: var(--ink);
  }
  .brand-mark {
    display: block;
    width: 46px;
    height: 46px;
    margin: 0 auto 22px;
    background: var(--brand-green);
  }
  .brand-name {
    font-size: 44px;
    font-weight: 600;
    line-height: 1;
    letter-spacing: -0.5px;
  }
  .brand-tagline {
    margin-top: 6px;
    font-size: 26px;
    font-weight: 600;
    letter-spacing: 6px;
  }

  .divider {
    position: absolute;
    left: 421px;
    top: 102px;
    width: 1px;
    height: 312px;
    background: linear-gradient(var(--card), var(--rule) 20%, var(--rule) 80%, var(--card));
  }

  .contact {
    position: absolute;
    left: 452px;
    top: 120px;
    color: var(--ink-soft);
  }
  .contact-name {
    font-size: 30px;
    font-weight: 600;
    color: var(--brand-green);
    line-height: 1.1;
  }
  .contact-title {
    font-size: 30px;
    font-weight: 600;
    color: var(--ink);
    line-height: 1.1;
  }
  .contact-details {
    list-style: none;
    margin-top: 64px;
    font-size: 20px;
    line-height: 26px;
  }
  .contact-details li { display: flex; align-items: center; }
  .contact-details .icon {
    width: 14px;
    height: 14px;
    margin-right: 6px;
    flex: none;
  }
  .contact-details .icon path,
  .contact-details .icon rect,
  .contact-details .icon circle { fill: var(--brand-green); }
</style>
</head>
<body>
  <article class="business-card">
    <div class="accent-band accent-band--top"></div>
    <div class="accent-band accent-band--bottom"></div>

    <div class="brand">
      <span class="brand-mark"></span>
      <div class="brand-name">BrookLamp</div>
      <div class="brand-tagline">Consulting</div>
    </div>

    <div class="divider"></div>

    <section class="contact">
      <h1 class="contact-name">Peter Varsiklo</h1>
      <h2 class="contact-title">Title</h2>
      <ul class="contact-details">
        <li>8276 Wimbrell Lane</li>
        <li>Dublin, OH 43092</li>
        <li>
          <svg class="icon" viewBox="0 0 16 16" aria-hidden="true">
            <path d="M3.5 1.5l2.6 0 1.2 3.3-1.7 1.2c.9 1.9 2.3 3.3 4.2 4.2l1.2-1.7 3.3 1.2v2.6c0 .8-.7 1.5-1.5 1.5C7 13.8 2.2 9 2 3c0-.8.7-1.5 1.5-1.5z"/>
          </svg>
          614-555-0172
        </li>
        <li>
          <svg class="icon" viewBox="0 0 16 16" aria-hidden="true">
            <path d="M1 3h14v10H1z M2.2 4.2v.4L8 8.6l5.8-4V4.2z" fill-rule="evenodd"/>
          </svg>
          pvarsiklo@brooklampconsulting.com
        </li>
        <li>
          <svg class="icon" viewBox="0 0 16 16" aria-hidden="true">
            <circle cx="8" cy="8" r="7"/>
          </svg>
          www.brooklampconsulting.com
        </li>
      </ul>
    </section>
  </article>
</body>
</html>
```